Business Card design for construction company

I would like a business card design for a construction company - Harlow Constructions. I have attached the ai logo file for use. I would like the card to be very smart and clean and incorporate only white and the two colours in the logo. I would like the card to have two sides. One side can just have the logo, the other with the relevant information.

Target Market(s)

Building and Construction Clients

Industry/Entity Type

Business

Contact Information for Business Card

Name: Tom Pardoe
Company: Harlow Constructions Pty Limited
Address: 14 Mallee Crescent Carrow Vale 2093
Phone: 0427 531 068
Email: tomp@harlowbuild-example.com.au

Font styles to use
Serif
Sans Serif

Requirements
Must have
• Details noted above
• Logo as provided
• Colours as in logo
• Square edges
• A font that compliments the logo
Should not have
• Any colour other than white and those in logo
• Rounded edges

```html
<!DOCTYPE html>
<html lang="en">
<head>
<meta charset="utf-8">
<title>Harlow Constructions — Business Card</title>
<link rel="stylesheet" href="https://fonts.googleapis.com/css2?family=Rajdhani:wght@500;600;700&display=swap">
<style>
  :root {
    --backdrop: #f3f6f7;
    --charcoal: #333333;
    --white: #ffffff;
    --aqua: #1fe6f2;
    --ink: #222222;
  }
  * { margin: 0; padding: 0; box-sizing: border-box; }
  html, body {
    width: 1200px;
    height: 529px;
    overflow: hidden;
    background: var(--backdrop);
    font-family: "Rajdhani", sans-serif;
  }
  .canvas {
    position: relative;
    width: 1200px;
    height: 529px;
  }
  .card {
    position: absolute;
    top: 115px;
    width: 520px;
    height: 300px;
  }
  .card--front {
    left: 59px;
    background: var(--charcoal);
    display: flex;
    align-items: center;
    justify-content: center;
  }
  .card--back {
    left: 619px;
    background: var(--white);
  }
  .wordmark {
    display: flex;
    align-items: center;
    gap: 14px;
  }
  .wordmark__dot {
    width: 10px;
    height: 10px;
    background: var(--aqua);
  }
  .wordmark__name {
    color: var(--white);
    font-weight: 500;
    font-size: 25px;
    letter-spacing: 2.5px;
    text-transform: uppercase;
  }
  .holder {
    position: absolute;
    left: 54px;
    top: 71px;
  }
  .holder__name {
    color: var(--aqua);
    font-weight: 700;
    font-size: 23px;
    line-height: 1;
  }
  .holder__company {
    margin-top: 6px;
    color: var(--ink);
    font-weight: 600;
    font-size: 12.5px;
  }
  .contacts {
    position: absolute;
    left: 235px;
    top: 156px;
    list-style: none;
  }
  .contacts__item {
    display: flex;
    align-items: center;
    gap: 9px;
    height: 24.5px;
    color: var(--ink);
    font-weight: 600;
    font-size: 13px;
  }
  .contacts__icon {
    width: 12px;
    height: 12px;
    flex: none;
    fill: var(--aqua);
  }
</style>
</head>
<body>
<main class="canvas">
  <section class="card card--front" aria-label="Card front">
    <div class="wordmark">
      <span class="wordmark__dot"></span>
      <span class="wordmark__name">Harlow Constructions</span>
    </div>
  </section>

  <section class="card card--back" aria-label="Card back">
    <div class="holder">
      <h1 class="holder__name">Tom Pardoe</h1>
      <p class="holder__company">Harlow Constructions Pty Limited</p>
    </div>
    <ul class="contacts">
      <li class="contacts__item">
        <svg class="contacts__icon" viewBox="0 0 24 24" aria-hidden="true"><path d="M6.6 10.8a15.1 15.1 0 0 0 6.6 6.6l2.2-2.2c.3-.3.7-.4 1-.2 1.1.4 2.3.6 3.6.6.6 0 1 .4 1 1V20c0 .6-.4 1-1 1C10.6 21 3 13.4 3 4c0-.6.4-1 1-1h3.5c.6 0 1 .4 1 1 0 1.3.2 2.5.6 3.6.1.3 0 .7-.2 1z"/></svg>
        <span>0427 531 068</span>
      </li>
      <li class="contacts__item">
        <svg class="contacts__icon" viewBox="0 0 24 24" aria-hidden="true"><path d="M2 5h20v14H2z M2 5l10 7 10-7" /><path d="M2 5l10 7 10-7v2l-10 7L2 7z" fill="#fff"/></svg>
        <span>tomp@harlowbuild-example.com.au</span>
      </li>
      <li class="contacts__item">
        <svg class="contacts__icon" viewBox="0 0 24 24" aria-hidden="true"><path d="M12 2a7 7 0 0 0-7 7c0 5.2 7 13 7 13s7-7.8 7-13a7 7 0 0 0-7-7zm0 9.5A2.5 2.5 0 1 1 12 6.5a2.5 2.5 0 0 1 0 5z"/></svg>
        <span>14 Mallee Crescent Carrow Vale 2093</span>
      </li>
    </ul>
  </section>
</main>
</body>
</html>
```